Health & Wellness Contest - The Bright Harvest Renewal

We need a postcard design that is professional and grabs the attention of people who see it. The postcard will be left in fitness centers and posted on social media. The front of the card MUST look amazing - make potential participants want to pick it up and find out more information; the back of the card will have the contest details. The goal is to have people sign up for a 90 day fitness program, and most of the marketing will be with this postcard.

Target Market(s)

People that are thinking about beginning a health regiment; people who are already used to exercising and are willing to try a new supplement

Industry/Entity Type

Health And Wellness

Colors

Designer to choose colors to be used in the design.

Requirements
Must have
• Front Cover -- Must have the phrase "The Bright Harvest Renewal" and must have "$2,500 Grand Prize"; and must have "BrightHarvestRenewal.com"
Nice to have
• Design on Front; Details on Back; appeal to both men and women

```html
<!DOCTYPE html>
<html lang="en">
<head>
<meta charset="UTF-8">
<title>The Bright Harvest Renewal – Postcard</title>
<link href="https://fonts.googleapis.com/css2?family=Poppins:wght@500;600;700&family=Open+Sans:wght@400;600&display=swap" rel="stylesheet">
<style>
  :root {
    --stage: #e4e4e4;
    --ink-black: #050505;
    --paper: #ffffff;
    --prize-blue: #1c3f6e;
    --logo-blue: #1f4a80;
    --rule-grey: #8a8a8a;
    --footer-grey: #6d6e70;
    --text-dark: #2b2b2b;
    --white: #ffffff;
  }
  * { box-sizing: border-box; margin: 0; padding: 0; }
  html, body {
    width: 1200px; height: 800px; overflow: hidden;
    background: var(--stage);
  }
  .sheet {
    width: 1200px; height: 800px;
    display: flex; align-items: center; justify-content: center; gap: 40px;
  }
  .postcard {
    width: 560px; height: 374px; position: relative; overflow: hidden;
    box-shadow: 0 6px 18px rgba(0,0,0,.18);
  }

  /* Front */
  .postcard--front { background: var(--ink-black); font-family: "Poppins", sans-serif; color: var(--white); }
  .front-photo {
    position: absolute; top: 0; right: 0; width: 282px; height: 100%;
    background: linear-gradient(100deg, #1a1110 0%, #5a2a1c 35%, #a05a3a 60%, #7a2a20 80%, #c4372c 100%);
  }
  .front-title { position: absolute; left: 34px; top: 40px; line-height: 1; }
  .front-title__lead { font-size: 34px; font-weight: 600; letter-spacing: -0.5px; }
  .front-title__main { font-size: 50px; font-weight: 700; letter-spacing: -1px; margin-top: 6px; }
  .front-title__sub { font-size: 34px; font-weight: 600; margin-top: 4px; }
  .prize-band {
    position: absolute; left: 0; top: 212px; width: 290px; height: 104px;
    background: var(--prize-blue); border-radius: 0 18px 18px 0;
    padding: 10px 0 0 34px; line-height: 1;
  }
  .prize-band__label { font-size: 16px; font-weight: 500; }
  .prize-band__amount { font-size: 54px; font-weight: 700; letter-spacing: -1px; margin-top: 4px; }
  .prize-band__deadline { font-size: 13px; font-weight: 500; margin-top: 4px; }
  .front-url { position: absolute; left: 34px; bottom: 22px; font-size: 15px; font-weight: 500; }

  /* Back */
  .postcard--back { background: var(--paper); font-family: "Open Sans", sans-serif; color: var(--text-dark); }
  .back-mission {
    position: absolute; left: 30px; top: 34px; width: 380px;
    font-size: 18px; font-weight: 600; line-height: 1.3;
  }
  .stamp-box {
    position: absolute; right: 30px; top: 24px; width: 86px; height: 86px;
    border: 2px solid var(--text-dark);
  }
  .back-divider { position: absolute; left: 0; right: 0; top: 130px; height: 3px; background: var(--rule-grey); }
  .back-partners { position: absolute; left: 30px; top: 160px; font-size: 14px; line-height: 1.4; width: 220px; }
  .sponsor-name {
    position: absolute; right: 34px; top: 160px;
    display: flex; align-items: center; gap: 10px;
    font-size: 20px; font-weight: 600; color: var(--logo-blue);
  }
  .sponsor-name__mark { width: 22px; height: 22px; background: var(--logo-blue); }
  .address-lines { position: absolute; left: 300px; right: 34px; top: 220px; }
  .address-lines span { display: block; height: 1px; background: var(--text-dark); margin-bottom: 28px; }
  .back-footer {
    position: absolute; left: 0; right: 0; bottom: 0; height: 64px;
    background: var(--footer-grey); color: var(--white);
    font-size: 14px; padding: 12px 30px; line-height: 1.45;
  }
</style>
</head>
<body>
<main class="sheet">
  <section class="postcard postcard--front" aria-label="Postcard front">
    <div class="front-photo" role="img" aria-label="Photo of a fit woman and man training with a dumbbell"></div>
    <h1 class="front-title">
      <div class="front-title__lead">The Bright</div>
      <div class="front-title__main">HARVEST</div>
      <div class="front-title__sub">RENEWAL</div>
    </h1>
    <div class="prize-band">
      <div class="prize-band__label">Challenge Grand Prize:</div>
      <div class="prize-band__amount">$2,500</div>
      <div class="prize-band__deadline">Register by October 31, 2017</div>
    </div>
    <div class="front-url">www.BrightHarvestRenewal.com</div>
  </section>

  <section class="postcard postcard--back" aria-label="Postcard back">
    <p class="back-mission">The Bright Harvest Renewal has one mission to help people be a better version of themselves.</p>
    <div class="stamp-box"></div>
    <div class="back-divider"></div>
    <p class="back-partners">A joint wellness experience shared between:</p>
    <div class="sponsor-name"><span class="sponsor-name__mark"></span>Ridgeline Law Group</div>
    <div class="address-lines"><span></span><span></span><span></span></div>
    <div class="back-footer">
      Questions? Reach us at Info@RidgelineLaw.Org.<br>
      or visit BrightHarvestRenewal.com
    </div>
  </section>
</main>
</body>
</html>
```